The name of the company is Dorvane Holdings, LLC. I would like a business card with a logo.

On the top left, I would like a logo design of a crown and I would like Dorvane over the top of the crown while Investments on the bottom. Please see attached files as an example of crown and positioning of Dorvane Holdings. Then I would like the letters DH in the middle(see picture).

Colors

Designer to choose colors to be used in the design.

```html
<!DOCTYPE html>
<html lang="en">
<head>
<meta charset="utf-8">
<title>Dorvane Holdings, LLC — Business Card</title>
<link rel="stylesheet" href="https://fonts.googleapis.com/css2?family=Montserrat:wght@400;700&display=swap">
<style>
  :root {
    --backdrop: #1e1e1e;
    --card-white: #ffffff;
    --charcoal: #3d3e40;
    --royal-blue: #0d4fa8;
    --ink-grey: #4a4a4a;
    --mark-white: #ffffff;
  }
  html, body {
    margin: 0;
    width: 1200px;
    height: 900px;
    overflow: hidden;
    background: var(--backdrop);
    font-family: "Montserrat", sans-serif;
  }
  .card {
    position: absolute;
    left: 100px;
    top: 165px;
    width: 1000px;
    height: 570px;
    background: var(--card-white);
    overflow: hidden;
  }
  .card-art {
    position: absolute;
    inset: 0;
  }
  .accent-bar {
    position: absolute;
    left: 0;
    top: 62px;
    width: 10px;
    height: 52px;
    background: var(--royal-blue);
  }
  .holder {
    position: absolute;
    left: 70px;
    top: 56px;
  }
  .holder-name {
    margin: 0;
    font-weight: 700;
    font-size: 32px;
    color: var(--royal-blue);
    letter-spacing: 0.5px;
  }
  .holder-title {
    margin: 0;
    font-size: 21px;
    color: var(--ink-grey);
  }
  .company {
    position: absolute;
    left: 70px;
    top: 185px;
    font-style: normal;
  }
  .company-name {
    margin: 0 0 4px;
    font-weight: 700;
    font-size: 23px;
    color: var(--royal-blue);
    letter-spacing: 1.2px;
    text-transform: uppercase;
  }
  .company-line {
    margin: 0;
    font-size: 21px;
    line-height: 1.3;
    color: var(--ink-grey);
    letter-spacing: 0.4px;
  }
  .contact {
    position: absolute;
    left: 60px;
    top: 350px;
    margin: 0;
    padding: 0;
    list-style: none;
  }
  .contact-item {
    display: flex;
    align-items: center;
    gap: 12px;
    font-size: 22px;
    color: var(--ink-grey);
    letter-spacing: 0.4px;
    line-height: 32px;
  }
  .contact-icon {
    width: 22px;
    height: 22px;
    flex: none;
  }
  .brand-mark {
    position: absolute;
    left: 695px;
    top: 165px;
    width: 270px;
    height: 270px;
    display: flex;
    align-items: center;
    justify-content: center;
    text-align: center;
    font-weight: 700;
    font-size: 27px;
    line-height: 1.3;
    letter-spacing: 2px;
    color: var(--mark-white);
    text-transform: uppercase;
  }
</style>
</head>
<body>
  <article class="card">
    <svg class="card-art" width="1000" height="570" viewBox="0 0 1000 570" aria-hidden="true">
      <circle cx="1000" cy="330" r="430" fill="var(--charcoal)"/>
      <path d="M 717 47 A 400 400 0 0 0 694 587 A 460 460 0 0 1 717 47 Z" fill="var(--royal-blue)"/>
      <circle cx="830" cy="300" r="135" fill="none" stroke="var(--mark-white)" stroke-width="2"/>
    </svg>

    <div class="accent-bar"></div>

    <header class="holder">
      <h1 class="holder-name">Teodor Vansell, MBA</h1>
      <p class="holder-title">Founder | CEO</p>
    </header>

    <address class="company">
      <p class="company-name">Dorvane Holdings, LLC</p>
      <p class="company-line">418 Larch Crest Road, Suite 200</p>
      <p class="company-line">Harbor Vale, CA. 90412</p>
    </address>

    <ul class="contact">
      <li class="contact-item">
        <svg class="contact-icon" viewBox="0 0 24 24" aria-hidden="true">
          <circle cx="12" cy="12" r="12" fill="var(--royal-blue)"/>
          <path d="M8.5 6.5c.6-.4 1.3-.3 1.6.3l1 1.8c.3.5.1 1.1-.3 1.4l-.8.6c.5 1.3 1.6 2.5 2.9 3l.6-.8c.4-.4 1-.5 1.4-.2l1.8 1c.6.3.7 1 .3 1.6-.8 1.1-2 1.5-3.3 1-3-1.2-5.4-3.6-6.4-6.6-.4-1.2.1-2.4 1.2-3.1z" fill="#fff"/>
        </svg>
        (555) 214-7730
      </li>
      <li class="contact-item">
        <svg class="contact-icon" viewBox="0 0 24 24" aria-hidden="true">
          <circle cx="12" cy="12" r="12" fill="var(--royal-blue)"/>
          <rect x="6" y="8" width="12" height="8.5" rx="1" fill="none" stroke="#fff" stroke-width="1.5"/>
          <path d="M6.5 8.5 12 13l5.5-4.5" fill="none" stroke="#fff" stroke-width="1.5"/>
        </svg>
        dorvane.holdings@mailbox.com
      </li>
    </ul>

    <div class="brand-mark">Dorvane<br>Holdings</div>
  </article>
</body>
</html>
```